Poster for Wobble Eve - a weekly comedy/variety show

We would like a poster/postcard design for a weekly alternative comedy/variety show called Wobble Eve.
Style: The poster should be fun and eye catching and very bold. It should have an alternative feel, not mainstream. Weird, strange, bizarre and funny is good. The show's title "Wobble Eve" should be very prominent. I like the idea of it being busy and cartoony, a collage of weirdness. Dusty Crumpet's Marching Parlour or Cpt. Tinsel's Quiet Lantern Bureau Choir or psychedelic rock posters of the 70's.
Design Specifics: We are looking for one design that can both be on an 11" x 17" poster and reduced to a 4" x 6" postcard.
The copy:
-
qvb productions presents:
Wobble Eve
standup, music, storytelling, sketch and improv
Wednesdays @ Lintmoth Theatre
5172 W. Harlowe - 2nd Floor
Chicago, IL 60689
7:30 - The Riffing Slot
8:30 - The Medley Stretch
9:45 - Pellbrook Loop
Pay what you want
website: wobbleeve.example
-
The back of the postcard can be very simple. We may add stickers to it regularly with the specific dates and the names of guest performers.
UPDATE: I've updated the copy a little bit and made this a guaranteed contest.
Updates
Reason: I asked a couple designers to submit changes and have extended the deadline so that they have time to do that.
I have picked a design and I'm just now going to try to choose between the variations of that poster that the designer posted. No need to add any more designs unless I request them directly.
Target Market(s)
Young adults (20s-40s), college students, living on the north side of Chicago who are looking for a fun, inexpensive, cool night out during the week.
Industry/Entity Type
Club
Look and feel
Each slider illustrates characteristics of the customer's brand and the style your logo design should communicate.

```html
<!DOCTYPE html>
<html lang="en">
<head>
<meta charset="utf-8">
<title>Wobble Eve — Weekly Comedy &amp; Variety Poster</title>
<link rel="stylesheet" href="https://fonts.googleapis.com/css2?family=Sancreek&family=Yanone+Kaffeesatz:wght@700&family=Barlow:wght@500&family=Poppins:wght@500&family=Caveat&family=Oswald:wght@700&display=swap">
<style>
  :root {
    --paper: #ffffff;
    --edge: #c9c9c9;
    --ink: #1e1e1e;
    --sky: #00aaea;
    --magenta: #c83d95;
    --navy: #34428a;
    --sun: #fff22e;
    --leaf: #2f9e55;
    --clay: #dc832d;
    --ember: #cf3f2b;
    --butter: #f4c934;
    --moss: #6aab50;
    --brick: #c0312f;
    --white: #ffffff;
  }
  html, body {
    margin: 0;
    width: 1200px;
    height: 1000px;
    overflow: hidden;
    background: var(--paper);
  }
  .poster { display: block; width: 1200px; height: 1000px; }
  .sheet { fill: var(--paper); stroke: var(--edge); stroke-width: 1; }
  .presenter, .acts { font-family: "Yanone Kaffeesatz", sans-serif; font-weight: 700; fill: var(--ink); }
  .presenter { font-size: 34px; }
  .acts { font-size: 30px; }
  .title-panel { fill: var(--sky); }
  .title { font-family: "Sancreek", serif; fill: var(--magenta); font-size: 190px; }
  .info-tab { fill: var(--ink); }
  .info-text { font-family: "Barlow", sans-serif; font-weight: 500; font-size: 15px; fill: var(--white); text-anchor: middle; }
  .art-sun { fill: var(--sun); }
  .art-leaf { fill: var(--leaf); opacity: .95; }
  .art-clay { fill: var(--clay); }
  .schedule-band { fill: var(--navy); }
  .schedule-overlap { fill: var(--ember); }
  .schedule { font-family: "Poppins", sans-serif; font-weight: 500; font-size: 32px; fill: var(--white); }
  .price-note { fill: var(--butter); }
  .price-text { font-family: "Caveat", cursive; font-size: 22px; fill: var(--ink); }
  .venue-box { fill: var(--moss); }
  .venue { font-family: "Oswald", sans-serif; font-weight: 700; fill: var(--brick); text-anchor: middle; }
  .venue-main { font-size: 22px; }
  .venue-address { font-size: 14px; }
</style>
</head>
<body>
<svg class="poster" viewBox="0 0 1200 1000" xmlns="http://www.w3.org/2000/svg">
  <rect class="sheet" x="323.5" y="36.5" width="595" height="918"/>

  <!-- title panel -->
  <polygon class="title-panel" points="323,97 745,60 790,565 346,600 323,600"/>

  <!-- artwork areas -->
  <path class="art-sun" role="img" aria-label="Yellow cartoon creature illustration"
        d="M760,160 C800,150 860,140 918,150 L918,420 C880,440 850,470 830,520 C815,570 800,600 760,605 C735,600 730,560 740,500 C750,420 745,300 760,160 Z"/>
  <path class="art-leaf" role="img" aria-label="Green cartoon figure illustration"
        d="M690,210 C720,180 760,190 765,240 C770,330 770,430 760,500 C755,540 720,552 680,550 C630,552 622,520 626,470 C630,400 620,320 640,270 C655,235 670,225 690,210 Z"/>

  <!-- title -->
  <g transform="rotate(-5 560 330)">
    <text class="title" x="355" y="325" textLength="370" lengthAdjust="spacingAndGlyphs">WOBBLE</text>
    <text class="title" x="390" y="510" textLength="320" lengthAdjust="spacingAndGlyphs">EVE</text>
  </g>

  <!-- info tab -->
  <rect class="info-tab" x="750" y="78" width="168" height="72"/>
  <text class="info-text" x="834" y="100" textLength="152" lengthAdjust="spacingAndGlyphs">visit: wobbleeve.example</text>
  <text class="info-text" x="834" y="120">for info on dates</text>
  <text class="info-text" x="834" y="140">and guests</text>

  <text class="presenter" x="352" y="86">qvb productions presents:</text>

  <text class="acts">
    <tspan x="765" y="403">improv,</tspan>
    <tspan x="765" y="437">standup,</tspan>
    <tspan x="765" y="471">music,</tspan>
    <tspan x="765" y="505">storytelling,</tspan>
    <tspan x="765" y="539">sketch</tspan>
    <tspan x="765" y="573">and more</tspan>
  </text>

  <!-- schedule band -->
  <rect class="schedule-band" x="447" y="585" width="471" height="188"/>
  <path class="art-clay" role="img" aria-label="Orange cartoon figure illustration"
        d="M410,578 C450,562 560,566 610,600 C660,640 700,700 690,770 C680,820 620,830 600,850 C650,880 740,880 740,910 C740,945 600,945 470,940 C400,938 360,920 365,880 C370,840 380,800 375,775 C400,740 400,700 405,660 C408,630 400,600 410,578 Z"/>
  <path class="schedule-overlap" d="M447,585 L570,585 C610,610 650,640 672,690 C690,730 690,760 688,773 L447,773 Z"/>
  <text class="schedule">
    <tspan x="478" y="643">7:30 - The Riffing Slot</tspan>
    <tspan x="478" y="688">8:30 - The Medley Stretch</tspan>
    <tspan x="478" y="732">9:45 - Pellbrook Loop</tspan>
  </text>

  <!-- price note -->
  <rect class="price-note" x="409" y="754" width="149" height="121"/>
  <text class="price-text">
    <tspan x="432" y="800">Pay what</tspan>
    <tspan x="432" y="830">you want</tspan>
    <tspan x="432" y="858">(min $3)</tspan>
  </text>

  <!-- venue -->
  <rect class="venue-box" x="733" y="742" width="155" height="213"/>
  <text class="venue venue-main">
    <tspan x="810" y="781">WEDNESDAYS</tspan>
    <tspan x="810" y="816">@ LINTMOTH</tspan>
    <tspan x="810" y="851">THEATRE</tspan>
  </text>
  <text class="venue venue-address">
    <tspan x="810" y="882">5172 W. HARLOWE</tspan>
    <tspan x="810" y="907">- 2ND FLOOR</tspan>
    <tspan x="810" y="932">CHICAGO, IL 60689</tspan>
  </text>
</svg>
</body>
</html>
```